New business card for our new logo

I have a brand new, existing logo. Now I need it on a new business card. The new card should include the following:

English language training
Translations
Interpreting Services (remote and in-person)

Target Market(s)

We are targeting international companies with foreign investment in the United States as well as domestic companies, medical offices, law offices, and non-profits that have non-native English speakers as their clients.

Contact Information for Business Card

Delia Brancombe, President
418 Garrow St.
Indianapolis, IN 46203
(317) 548-3162
info@tallpinewordworks.com
www.tallpinewordworks.com

Font styles to use
Sans Serif

Colors
0392cd
3176b5
abd036
9bcb3b
f04a50
f78f20

Requirements
Must have
• It must include our logo and business card details
Nice to have
• I would like to see a layout that is uncluttered and conveys trust and dependability, as well as the feelings of being friendly and approachable.

It would be nice to have icons for English language training, translating, and interpreting.
Should not have
• No pink, yellow, or purple

```html
<!DOCTYPE html>
<html lang="en">
<head>
<meta charset="utf-8">
<title>Tall Pine Wordworks – Business Card</title>
<link rel="stylesheet" href="https://fonts.googleapis.com/css2?family=Montserrat:wght@700&family=Roboto:wght@400&display=swap">
<style>
  :root {
    --stage: #26282b;
    --blue: #3f74bb;
    --blue-light: #6b97cf;
    --blue-deep: #3a6cb6;
    --white: #ffffff;
    --ink: #5d6066;
    --rule: #8a8d92;
  }
  * { box-sizing: border-box; margin: 0; padding: 0; }
  html, body { width: 1200px; height: 929px; overflow: hidden; }
  body {
    background: var(--stage);
    display: flex;
    align-items: center;
    justify-content: center;
    gap: 40px;
    font-family: "Roboto", Arial, sans-serif;
  }
  .card {
    position: relative;
    width: 540px;
    height: 309px;
    overflow: hidden;
    box-shadow: 0 10px 28px rgba(0,0,0,.45);
  }

  /* Front */
  .card--front {
    background: linear-gradient(135deg, var(--blue-deep) 0%, var(--blue) 40%, var(--blue-light) 100%);
    color: var(--white);
  }
  .front-brand {
    position: absolute;
    left: 92px;
    top: 70px;
    display: flex;
    align-items: center;
    gap: 18px;
  }
  .brand-dot {
    width: 104px;
    height: 104px;
    border-radius: 50%;
    background: var(--white);
    flex: none;
  }
  .brand-name {
    font-family: "Montserrat", Arial, sans-serif;
    font-weight: 700;
    font-size: 33px;
    line-height: 1.02;
    letter-spacing: .5px;
  }
  .brand-name span { display: block; }
  .brand-name span:nth-child(2) { padding-left: 16px; }
  .brand-name span:nth-child(3) { padding-left: 32px; }
  .services {
    position: absolute;
    left: 0;
    right: 0;
    bottom: 46px;
    display: flex;
    justify-content: center;
    gap: 14px;
    font-size: 12.5px;
    letter-spacing: .2px;
    list-style: none;
  }
  .services li::before {
    content: "";
    display: inline-block;
    width: 6px;
    height: 6px;
    border-radius: 50%;
    background: var(--white);
    margin-right: 5px;
    vertical-align: middle;
  }

  /* Back */
  .card--back { background: var(--white); color: var(--ink); }
  .back-brand {
    position: absolute;
    left: 52px;
    top: 48px;
    display: flex;
    align-items: center;
    gap: 12px;
    color: var(--blue);
  }
  .back-brand .brand-dot { width: 82px; height: 82px; background: var(--blue); }
  .back-brand .brand-name { font-size: 24px; }
  .back-brand .brand-name span:nth-child(2) { padding-left: 12px; }
  .back-brand .brand-name span:nth-child(3) { padding-left: 24px; }
  .accent-tab {
    position: absolute;
    right: 0;
    top: 98px;
    width: 10px;
    height: 24px;
    background: var(--blue);
  }
  .person {
    position: absolute;
    right: 34px;
    top: 92px;
    text-align: right;
  }
  .person-name {
    font-family: "Montserrat", Arial, sans-serif;
    font-weight: 700;
    font-size: 20px;
    color: var(--blue);
  }
  .person-title {
    font-family: "Montserrat", Arial, sans-serif;
    font-weight: 700;
    font-size: 14.5px;
    color: var(--ink);
    margin-top: 1px;
  }
  .divider {
    position: absolute;
    left: 100px;
    top: 176px;
    width: 300px;
    height: 1px;
    background: var(--rule);
  }
  .contacts {
    position: absolute;
    right: 20px;
    top: 176px;
    list-style: none;
    font-size: 12.5px;
    line-height: 19px;
    text-align: right;
  }
  .contacts li { display: flex; align-items: center; justify-content: flex-end; gap: 6px; }
  .contacts svg { width: 13px; height: 13px; fill: none; stroke: var(--blue); stroke-width: 2; flex: none; }
  .contacts .icon-solid { fill: var(--blue); stroke: none; }
  .address {
    position: absolute;
    left: 96px;
    bottom: 40px;
    font-style: normal;
    font-size: 14px;
    line-height: 18px;
    color: var(--ink);
  }
</style>
</head>
<body>

  <section class="card card--front" aria-label="Card front">
    <div class="front-brand">
      <div class="brand-dot"></div>
      <h1 class="brand-name"><span>Tall Pine</span><span>Wordworks</span></h1>
    </div>
    <ul class="services">
      <li>English language training</li>
      <li>Translations</li>
      <li>Interpreting Services</li>
    </ul>
  </section>

  <section class="card card--back" aria-label="Card back">
    <div class="back-brand">
      <div class="brand-dot"></div>
      <h2 class="brand-name"><span>Tall Pine</span><span>Wordworks</span></h2>
    </div>
    <div class="accent-tab"></div>
    <div class="person">
      <p class="person-name">Delia Brancombe</p>
      <p class="person-title">President</p>
    </div>
    <div class="divider"></div>
    <ul class="contacts">
      <li>(317) 548-3162
        <svg viewBox="0 0 24 24" aria-hidden="true"><path class="icon-solid" d="M6.6 10.8a15 15 0 0 0 6.6 6.6l2.2-2.2a1 1 0 0 1 1-.25 11.4 11.4 0 0 0 3.6.57 1 1 0 0 1 1 1V20a1 1 0 0 1-1 1A17 17 0 0 1 3 4a1 1 0 0 1 1-1h3.5a1 1 0 0 1 1 1c0 1.25.2 2.45.57 3.57a1 1 0 0 1-.25 1z"/></svg>
      </li>
      <li>info@tallpinewordworks.com
        <svg viewBox="0 0 24 24" aria-hidden="true"><rect class="icon-solid" x="2" y="5" width="20" height="14" rx="1"/><path d="M3 6l9 7 9-7" stroke="#fff"/></svg>
      </li>
      <li>www.tallpinewordworks.com
        <svg viewBox="0 0 24 24" aria-hidden="true"><circle cx="12" cy="12" r="9.5"/><path d="M2.5 12h19M12 2.5c3 3 3 16 0 19M12 2.5c-3 3-3 16 0 19"/></svg>
      </li>
    </ul>
    <address class="address">418 Garrow St.<br>Indianapolis, IN 46203</address>
  </section>

</body>
</html>
```